PR & Jobs Workshop

We need a eye catching poster design (standard size) to attract people to register and attend a workshop. These will be posted in cafes, notice boards, grocery stores across the city.
Target Market(s)
Target audience is young people between 20-35 age.
Colors
Designer to choose colors to be used in the design.
Requirements
Must have
- (Main Heading)
- Free Jobs & PR Workshop
- (Body)
- What & Who
- - Where & how will I find jobs?
- - What jobs will lead to PR?
- - When & how can my family join me?
- - How much salary do I need?
- - I have a job, do I qualify for PR?
- - I don't have a job, do I qualify for PR?
- To get answers to all these questions, attend a FREE Jobs & PR Workshop by your Friendly & Frank Licensed Immigration Adviser, Dev Malhotra.
- License No: 304718952
- When & Where
- On Sunday, 30 September 2018
- 12-2 pm @ TBC
- TEXT "REGISTER" to 022 487 3920
- LIMITED SEATS ONLY
- (Add photo along with below text)
- Search for 'Dev Malhotra' on ClipHub
- (Add logo along with below text)
- www.qrtworldwide.com
Nice to have
- Classy
Should not have
- Avoid too many colors

```html
<!DOCTYPE html>
<html lang="en">
<head>
<meta charset="utf-8">
<title>Free Jobs &amp; PR Workshop</title>
<link href="https://fonts.googleapis.com/css2?family=Roboto+Condensed:ital,wght@0,300;0,400;0,700;0,900;1,900&display=swap" rel="stylesheet">
<style>
  :root {
    --backdrop: #c0c0c0;
    --orange: #ff5000;
    --ink: #0a0a0a;
    --paper: #ffffff;
    --photo-tone: #5a4a44;
  }
  * { margin: 0; padding: 0; box-sizing: border-box; }
  html, body { width: 1200px; height: 1200px; overflow: hidden; }
  body {
    background: var(--backdrop);
    font-family: "Roboto Condensed", "Arial Narrow", sans-serif;
    position: relative;
  }
  .poster {
    position: absolute;
    left: 254px; top: 79px;
    width: 692px; height: 1038px;
    background: var(--paper);
    overflow: hidden;
  }
  .poster__band { position: absolute; left: 0; top: 0; width: 692px; height: 830px; }
  .poster > *:not(.poster__band) { position: absolute; white-space: nowrap; }

  .title {
    left: 0; width: 692px; top: 48px;
    text-align: center;
    font-weight: 900; font-style: italic;
    font-size: 88px; line-height: 72px;
    letter-spacing: -2px;
    color: var(--ink);
    text-transform: uppercase;
  }
  .title span { display: block; }
  .title span:first-child { padding-left: 14px; }

  .question { color: var(--paper); font-weight: 700; letter-spacing: -0.3px; }
  .q1 { left: 140px; top: 214px; font-size: 40px; }
  .q2 { left: 212px; top: 264px; font-size: 32px; }
  .q3 { left: 58px;  top: 308px; font-size: 27px; }
  .q4 { left: 152px; top: 346px; font-size: 40px; }
  .q5 { left: 96px;  top: 393px; font-size: 31px; }
  .q6 { left: 240px; top: 434px; font-size: 37px; }

  .intro {
    left: 0; width: 692px; top: 488px;
    text-align: center;
    font-weight: 300; font-size: 25px; line-height: 28px;
    color: var(--ink);
  }
  .intro strong { font-weight: 700; }

  .when {
    left: 0; width: 692px; top: 621px;
    text-align: center; font-size: 25px; color: var(--ink); font-weight: 300;
  }
  .when strong { font-weight: 700; }
  .when .divider { margin: 0 12px; }

  .register {
    left: 124px; top: 664px; width: 448px; height: 39px;
    background: var(--ink); color: var(--paper);
    font-weight: 700; font-size: 27px; line-height: 39px;
    text-align: center;
  }
  .seats {
    left: 0; width: 692px; top: 720px;
    text-align: center; font-weight: 300; font-size: 24px; color: var(--ink);
  }

  .brand { left: 62px; top: 856px; width: 210px; text-align: center; color: var(--ink); }
  .brand__name { display: block; font-weight: 900; font-size: 76px; line-height: 76px; }
  .brand__tag { display: block; font-weight: 900; font-size: 12px; letter-spacing: 0.3px; }
  .website {
    left: 48px; width: 240px; top: 964px; text-align: center;
    color: var(--orange); font-weight: 400; font-size: 26px; letter-spacing: 0.8px;
  }

  .portrait { left: 338px; top: 874px; width: 93px; height: 92px; background: linear-gradient(160deg, #8a7b72, var(--photo-tone) 60%, #1d1d1d); }

  .channel {
    left: 449px; top: 878px; width: 200px; text-align: center;
    font-weight: 900; font-style: italic; font-size: 24px; line-height: 21px;
    color: var(--ink); text-transform: uppercase;
  }
  .channel__name {
    left: 490px; top: 931px;
    display: flex; align-items: center; gap: 6px;
    font-weight: 700; font-size: 34px; line-height: 34px; color: var(--ink);
    letter-spacing: -0.5px;
  }
  .channel__dot { width: 24px; height: 24px; border-radius: 50%; background: var(--orange); }
</style>
</head>
<body>
  <main class="poster">
    <svg class="poster__band" width="692" height="830" viewBox="0 0 692 830" aria-hidden="true">
      <polygon points="0,0 692,0 692,773 0,827" fill="var(--orange)"/>
    </svg>

    <h1 class="title"><span>Free Jobs &amp;</span><span>PR Workshop</span></h1>

    <p class="question q1">Where &amp; how will I find jobs?</p>
    <p class="question q2">How much salary do I need?</p>
    <p class="question q3">When &amp; how can my family join me?</p>
    <p class="question q4">I have a job, do I qualify for PR?</p>
    <p class="question q5">I don't have a job, do I qualify for PR?</p>
    <p class="question q6">What jobs will lead to PR?</p>

    <p class="intro">To get answers to all these questions,<br>
      attend a <strong>FREE Jobs &amp; PR Workshop</strong> by your<br>
      Friendly &amp; Frank Licensed Immigration Adviser, Dev Malhotra.<br>
      License No: 304718952</p>

    <p class="when"><strong>On Sunday, 30 September 2018</strong><span class="divider">|</span>12-2 pm @ TBC</p>

    <p class="register">TEXT "REGISTER" to 022 487 3920</p>
    <p class="seats">LIMITED SEATS ONLY.</p>

    <div class="brand">
      <span class="brand__name">QRT</span>
      <span class="brand__tag">GLOBAL EDUCATION ADVICE</span>
      <span class="brand__tag">ACCURATE | LICENSED | 24/7</span>
    </div>
    <p class="website">www.qrtworldwide.com</p>

    <div class="portrait" role="img" aria-label="Portrait photo of adviser Dev Malhotra"></div>

    <p class="channel">Search for<br>'Dev Malhotra' on</p>
    <p class="channel__name"><span class="channel__dot"></span>ClipHub</p>
  </main>
</body>
</html>
```